Velora Aesthetica

Medical doctor providing aesthetic medicine

* Double sided card
* Logo to be on card
Other details:
* Dr. Mirela Kostvan, BSc, MBChB, CCFP
* #214-215, 27903 83 Ave, Surrey, BC, V2T 4K7
* 604-718-2943
* info@veloraclinic.ca
* www.veloraclinic.ca

Industry/Entity Type

Medical / Health & Beauty

Contact Information for Business Card

see 'Project Description'

Colors
0054AA
0677BA
7BADD7
CADEEF
E8F1F8
FFF300
FFF600
FEFA6F
FFFEC7
FFFEE8

Requirements
Must have
• Modern, high-end design

```html
<!DOCTYPE html>
<html lang="en">
<head>
<meta charset="utf-8">
<title>Velora Aesthetica – Business Card</title>
<link rel="stylesheet" href="https://fonts.googleapis.com/css2?family=Montserrat:wght@300;400;500;800&display=swap">
<style>
  :root {
    --navy: #24415f;
    --navy-pattern: #284767;
    --white: #ffffff;
    --gold: #f7c614;
    --gold-soft: #d9ae2e;
    --icon-ink: #111111;
  }
  * { box-sizing: border-box; margin: 0; padding: 0; }
  html, body { width: 1200px; height: 720px; overflow: hidden; background: var(--navy); }
  .card {
    position: relative;
    width: 1200px;
    height: 720px;
    background: var(--navy);
    font-family: "Montserrat", Arial, sans-serif;
    color: var(--white);
    overflow: hidden;
  }
  .card__pattern {
    position: absolute;
    inset: 0;
    background: radial-gradient(circle at 55% 45%, var(--navy-pattern) 0%, var(--navy) 70%);
  }
  .brand {
    position: absolute;
    left: 60px;
    width: 540px;
    top: 160px;
    text-align: center;
  }
  .brand__ring {
    display: block;
    width: 120px;
    height: 120px;
    margin: 0 auto 48px;
    border: 3px solid var(--gold-soft);
    border-radius: 50%;
  }
  .brand__name {
    font-weight: 500;
    color: var(--white);
    line-height: 1;
  }
  .brand__name-main {
    display: block;
    font-size: 78px;
    letter-spacing: 0.32em;
    margin-right: -0.32em;
  }
  .brand__name-sub {
    display: block;
    font-size: 28px;
    letter-spacing: 0.55em;
    margin-right: -0.55em;
    margin-top: 22px;
  }
  .doctor {
    position: absolute;
    left: 624px;
    top: 118px;
  }
  .doctor__name {
    font-weight: 800;
    font-size: 46px;
    letter-spacing: 0.01em;
    line-height: 1;
  }
  .doctor__credentials {
    position: absolute;
    top: 66px;
    left: 0;
    font-weight: 400;
    font-size: 30px;
    color: var(--gold);
    white-space: nowrap;
  }
  .doctor__rule {
    position: absolute;
    left: 944px;
    right: 0;
    top: 194px;
    height: 3px;
    background: var(--white);
  }
  .contact {
    position: absolute;
    left: 619px;
    top: 290px;
    list-style: none;
  }
  .contact__item {
    position: absolute;
    left: 0;
    display: flex;
    align-items: flex-start;
    white-space: nowrap;
  }
  .contact__icon {
    flex: none;
    width: 44px;
    height: 44px;
    border-radius: 50%;
    background: var(--gold);
    display: flex;
    align-items: center;
    justify-content: center;
  }
  .contact__icon svg { width: 24px; height: 24px; }
  .contact__text {
    margin-left: 21px;
    font-weight: 300;
    font-size: 26px;
    line-height: 33px;
    padding-top: 5px;
  }
  .contact__item--phone { top: 0; }
  .contact__item--email { top: 55px; }
  .contact__item--web { top: 110px; }
  .contact__item--address { top: 165px; }
</style>
</head>
<body>
<main class="card">
  <div class="card__pattern" role="img" aria-label="Faint pattern of medical icons on navy background"></div>

  <div class="brand">
    <span class="brand__ring"></span>
    <p class="brand__name">
      <span class="brand__name-main">VELORA</span>
      <span class="brand__name-sub">AESTHETICA</span>
    </p>
  </div>

  <header class="doctor">
    <h1 class="doctor__name">DR. MIRELA KOSTVAN</h1>
    <p class="doctor__credentials">BSC, MBCHB, CCFP</p>
  </header>
  <div class="doctor__rule"></div>

  <ul class="contact">
    <li class="contact__item contact__item--phone">
      <span class="contact__icon">
        <svg viewBox="0 0 24 24" aria-hidden="true"><path fill="#111" d="M3 9c0-2 3-4 9-4s9 2 9 4v2h-4V9c-1-.7-3-1-5-1s-4 .3-5 1v2H3z"/><path fill="#111" d="M7 11l2-2h6l2 2 2 7H5z"/><g fill="#f7c614"><rect x="9" y="12" width="1.5" height="1.5"/><rect x="11.25" y="12" width="1.5" height="1.5"/><rect x="13.5" y="12" width="1.5" height="1.5"/><rect x="9" y="14.5" width="1.5" height="1.5"/><rect x="11.25" y="14.5" width="1.5" height="1.5"/><rect x="13.5" y="14.5" width="1.5" height="1.5"/></g></svg>
      </span>
      <span class="contact__text">604-718-2943</span>
    </li>
    <li class="contact__item contact__item--email">
      <span class="contact__icon">
        <svg viewBox="0 0 24 24" aria-hidden="true"><rect x="3" y="6" width="18" height="13" fill="#111"/><path d="M4 7l8 6 8-6M4 18l6-5M20 18l-6-5" stroke="#f7c614" stroke-width="1.2" fill="none"/></svg>
      </span>
      <span class="contact__text">info@veloraclinic.ca</span>
    </li>
    <li class="contact__item contact__item--web">
      <span class="contact__icon">
        <svg viewBox="0 0 24 24" aria-hidden="true"><g fill="none" stroke="#111" stroke-width="1.6"><circle cx="12" cy="12" r="9"/><ellipse cx="12" cy="12" rx="4" ry="9"/><path d="M3 12h18M4.5 7.5h15M4.5 16.5h15M12 3v18"/></g></svg>
      </span>
      <span class="contact__text">www.veloraclinic.ca</span>
    </li>
    <li class="contact__item contact__item--address">
      <span class="contact__icon">
        <svg viewBox="0 0 24 24" aria-hidden="true"><path fill="#111" d="M12 2a7 7 0 0 0-7 7c0 5 7 13 7 13s7-8 7-13a7 7 0 0 0-7-7z"/><circle cx="12" cy="9" r="2.6" fill="#f7c614"/></svg>
      </span>
      <span class="contact__text">#214-215, 27903 83 Ave, Surrey,<br>BC, V2T 4K7</span>
    </li>
  </ul>
</main>
</body>
</html>
```